Brit Rock covers band "The Tin Kettles" requires poster for Marlowe Lounge Friday March 31st

I want a design for a poster (A3 and A4) and Facebook/Instagram ads.
Primary focus is the band name logo "The Tin Kettles", style as in attached file, followed by tag "Old Skool Brit Rock".
Backdrop to be 60's psychedelic art.
Secondary focus is the venue "The Marlowe Lounge"
Supporting text to include:
- 27 Fenwick Road, Chatswood SYDNEY
- Friday 31st March 2023
- 7:00 pm until late
- Bar sales refreshments
- NO admission fee

```html
<!DOCTYPE html>
<html lang="en">
<head>
<meta charset="utf-8">
<title>The Tin Kettles – Old Skool Brit Rock at The Marlowe Lounge</title>
<link rel="stylesheet" href="https://fonts.googleapis.com/css2?family=Exo+2:wght@700;800&family=Gochi+Hand&display=swap">
<style>
  :root {
    --paper: #ede9d8;
    --ink: #262626;
    --sun: #f4a824;
    --band: #252525;
  }
  html, body {
    margin: 0;
    padding: 0;
    width: 849px;
    height: 1200px;
    overflow: hidden;
    background: var(--paper);
  }
  .poster {
    position: relative;
    width: 849px;
    height: 1200px;
    overflow: hidden;
    background: radial-gradient(ellipse at 30% 40%, #f2eee0 0%, var(--paper) 70%);
    font-family: "Exo 2", sans-serif;
    color: var(--ink);
  }
  .artwork {
    position: absolute;
    left: 0;
    top: 0;
    width: 849px;
    height: 760px;
  }
  .band-name {
    position: absolute;
    left: 78px;
    top: 500px;
    margin: 0;
    font-family: "Exo 2", sans-serif;
    font-weight: 800;
    color: var(--ink);
    line-height: 1;
    text-transform: uppercase;
  }
  .band-name .line-one {
    display: block;
    font-size: 104px;
    letter-spacing: -3px;
  }
  .band-name .line-two {
    display: block;
    font-size: 122px;
    letter-spacing: -4px;
    margin-left: 60px;
    margin-top: 2px;
  }
  .tagline {
    position: absolute;
    left: 240px;
    top: 784px;
    margin: 0;
    font-family: "Gochi Hand", cursive;
    font-size: 38px;
    letter-spacing: 6px;
    color: var(--ink);
    text-shadow: 2px 2px 0 var(--sun);
  }
  .venue-band {
    position: absolute;
    left: 0;
    top: 938px;
    width: 849px;
    height: 37px;
    background: var(--band);
    display: flex;
    align-items: center;
    justify-content: center;
  }
  .venue-name {
    margin: 0;
    font-family: "Exo 2", sans-serif;
    font-weight: 700;
    font-size: 24px;
    letter-spacing: 6px;
    color: var(--sun);
  }
  .details {
    position: absolute;
    top: 1008px;
    left: 0;
    width: 849px;
    margin: 0;
    padding: 0;
    list-style: none;
  }
  .detail {
    position: absolute;
    top: 0;
    width: 150px;
    margin-left: -75px;
    text-align: center;
  }
  .detail svg {
    display: block;
    margin: 0 auto;
    width: 74px;
    height: 74px;
  }
  .detail-text {
    margin: 12px 0 0;
    font-weight: 700;
    font-size: 16.5px;
    line-height: 26px;
    color: var(--ink);
    white-space: nowrap;
  }
  .detail--where { left: 170px; }
  .detail--date  { left: 317px; }
  .detail--time  { left: 441px; }
  .detail--bar   { left: 567px; }
  .detail--entry { left: 705px; }
</style>
</head>
<body>
<main class="poster">

  <svg class="artwork" viewBox="0 0 849 760" role="img"
       aria-label="Illustration: a black hand making the rock horns gesture, formed as a guitar headstock with tuning pegs and strings, in front of a large orange sun">
    <circle cx="427" cy="427" r="318" fill="var(--sun)"/>
  </svg>

  <h1 class="band-name">
    <span class="line-one">The Tin</span>
    <span class="line-two">Kettles</span>
  </h1>

  <p class="tagline">"Old Skool Brit Rock"</p>

  <div class="venue-band">
    <h2 class="venue-name">”The Marlowe Lounge”</h2>
  </div>

  <ul class="details">
    <li class="detail detail--where">
      <svg viewBox="0 0 74 74" aria-hidden="true">
        <path d="M37 66 C30 54 18 42 18 28 a19 19 0 0 1 38 0 C56 42 44 54 37 66 Z"
              fill="none" stroke="var(--ink)" stroke-width="2.6" stroke-linejoin="round"/>
        <circle cx="37" cy="28" r="7.5" fill="none" stroke="var(--sun)" stroke-width="3"/>
      </svg>
      <p class="detail-text">27 Fenwick Road,<br>Chatswood SYDNEY</p>
    </li>

    <li class="detail detail--date">
      <svg viewBox="0 0 74 74" aria-hidden="true">
        <rect x="6" y="12" width="50" height="40" rx="2" fill="none" stroke="var(--ink)" stroke-width="2.4"/>
        <line x1="6" y1="21" x2="56" y2="21" stroke="var(--ink)" stroke-width="2"/>
        <g stroke="var(--ink)" stroke-width="2">
          <line x1="11" y1="9" x2="11" y2="15"/><line x1="17" y1="9" x2="17" y2="15"/>
          <line x1="23" y1="9" x2="23" y2="15"/><line x1="29" y1="9" x2="29" y2="15"/>
          <line x1="35" y1="9" x2="35" y2="15"/><line x1="41" y1="9" x2="41" y2="15"/>
          <line x1="47" y1="9" x2="47" y2="15"/><line x1="53" y1="9" x2="53" y2="15"/>
        </g>
        <g stroke="var(--ink)" stroke-width="2.2" stroke-dasharray="3 2.5">
          <line x1="11" y1="28" x2="50" y2="28"/>
          <line x1="11" y1="34" x2="44" y2="34"/>
          <line x1="11" y1="40" x2="40" y2="40"/>
          <line x1="11" y1="46" x2="36" y2="46"/>
        </g>
        <circle cx="55" cy="52" r="12" fill="var(--paper)" stroke="var(--ink)" stroke-width="2.4"/>
        <path d="M55 45 V52 H60" fill="none" stroke="var(--sun)" stroke-width="2.4"/>
      </svg>
      <p class="detail-text">Friday 31st<br>March 2023</p>
    </li>

    <li class="detail detail--time">
      <svg viewBox="0 0 74 74" aria-hidden="true">
        <circle cx="37" cy="37" r="28" fill="none" stroke="var(--ink)" stroke-width="2.6"/>
        <circle cx="37" cy="37" r="23" fill="none" stroke="var(--ink)" stroke-width="1.2"/>
        <path d="M37 22 V40 H30" fill="none" stroke="var(--sun)" stroke-width="2.6"/>
      </svg>
      <p class="detail-text">7:00 pm<br>until late</p>
    </li>

    <li class="detail detail--bar">
      <svg viewBox="0 0 74 74" aria-hidden="true">
        <path d="M14 36 h16 c0 10 -3 16 -8 16 s-8 -6 -8 -16 Z" fill="none" stroke="var(--ink)" stroke-width="2.4"/>
        <line x1="15" y1="42" x2="29" y2="42" stroke="var(--sun)" stroke-width="2.4"/>
        <line x1="22" y1="52" x2="22" y2="66" stroke="var(--ink)" stroke-width="2.4"/>
        <line x1="16" y1="66" x2="28" y2="66" stroke="var(--ink)" stroke-width="2.4"/>
        <path d="M44 6 h8 v16 c6 4 7 9 7 14 v30 h-22 v-30 c0 -5 1 -10 7 -14 Z"
              fill="none" stroke="var(--ink)" stroke-width="2.4" stroke-linejoin="round"/>
        <line x1="44" y1="11" x2="52" y2="11" stroke="var(--ink)" stroke-width="2"/>
        <line x1="42" y1="46" x2="54" y2="46" stroke="var(--sun)" stroke-width="2.4"/>
        <line x1="44" y1="52" x2="52" y2="52" stroke="var(--sun)" stroke-width="2.4"/>
      </svg>
      <p class="detail-text">Bar sales<br>refreshments</p>
    </li>

    <li class="detail detail--entry">
      <svg viewBox="0 0 74 74" aria-hidden="true">
        <rect x="14" y="30" width="50" height="28" fill="none" stroke="var(--ink)" stroke-width="2"/>
        <rect x="11" y="26" width="50" height="28" fill="var(--paper)" stroke="var(--ink)" stroke-width="2"/>
        <rect x="8" y="22" width="50" height="28" fill="var(--paper)" stroke="var(--ink)" stroke-width="2.4"/>
        <rect x="13" y="27" width="40" height="18" rx="2" fill="none" stroke="var(--ink)" stroke-width="1.6"/>
        <circle cx="33" cy="36" r="5" fill="none" stroke="var(--sun)" stroke-width="2.4"/>
        <line x1="18" y1="36" x2="24" y2="36" stroke="var(--sun)" stroke-width="2.4"/>
        <line x1="42" y1="36" x2="48" y2="36" stroke="var(--sun)" stroke-width="2.4"/>
      </svg>
      <p class="detail-text">NO<br>admission fee</p>
    </li>
  </ul>

</main>
</body>
</html>
```